Mobile app for checking bus arrival

I would like to make the UI much more beautiful and modern. The app is an app to check bus arrival in Singapore.
See here: https://apps.veltrixa.com/store/apps/details?id=com.ridetrk&hl=en

Based on the question from designers:

1. The first screen shows the favorite bus stop. Each item shows location / street, the top one is the location, second line is the street name. And the number is the bus stop code.

2. Please download the app and try bus stop code with 07589 or 10079, for example. It will bring you to the next screen.

3. The pencil allow you to select color theme, for the list item, and the header.

4. On the second screen, it will show up the list of bus route that available on that bus stop.

5. When you tap on one of them it will show you the 2 subsequent arrival time.

6. Each of the arrival time has the information of availability seats available, seats not available, no more space. (we can use green, yellow, red, respectively).

7. Each of the arrival time has the WAB indicator (Wheelchair availability). Show as icon is preferred.

7. KLV and DPWQ are the bus provider in Singapore. 48 means the route /service no.

Requirements:
And check the attachment, see screen 3. I need to add information about the space availability, which has 3 state: seats available, seats not available, no more space. (we can use green, yellow, red, respectively).

Please advise how to show the information.

Target Market(s)

Students, age below 35

Industry/Entity Type

Veltrixa

Requirements
Must have
• The app currently has the capabilities to select color theme, checkout screen1. It's the button and the list item color.
Nice to have
• Please download the app to see all available colors, and make suggestion to have better color pallete.

```html
<!DOCTYPE html>
<html lang="en">
<head>
<meta charset="utf-8">
<title>Bus Stop 07589 – Arrivals</title>
<link rel="stylesheet" href="https://fonts.googleapis.com/css2?family=Montserrat:wght@300;400;500&display=swap">
<style>
  :root {
    --page-bg: #474a52;
    --header-blue: #4a7ef0;
    --subbar-blue: #5b8af2;
    --tile-red: #e44a48;
    --tile-purple: #9b45e0;
    --tile-grey: #ececec;
    --tile-white: #ffffff;
    --text-light: #ffffff;
    --seat-available: #35c46a;
    --seat-standing: #f4c430;
    --seat-full: #c4161c;
    --ad-dark: #a8561a;
    --ad-light: #f0a23a;
  }
  * { box-sizing: border-box; margin: 0; padding: 0; }
  html, body {
    width: 1200px; height: 900px; overflow: hidden;
    background: var(--page-bg);
    font-family: "Montserrat", sans-serif;
  }
  .icon-defs { position: absolute; width: 0; height: 0; }
  .app-screen {
    position: absolute; left: 370px; top: 41px;
    width: 461px; height: 818px;
    background: var(--tile-white);
    overflow: hidden;
    box-shadow: 0 20px 60px rgba(0,0,0,.35);
  }
  .status-bar {
    height: 29px; background: var(--header-blue); color: var(--text-light);
    display: flex; align-items: center; justify-content: space-between;
    padding: 0 10px; font-size: 13px; font-weight: 400;
  }
  .status-bar .carrier { display: flex; align-items: center; gap: 5px; }
  .status-bar .dots { letter-spacing: 1px; font-size: 9px; }
  .status-bar .battery { display: flex; align-items: center; gap: 5px; }
  .battery-icon { width: 24px; height: 11px; border: 1px solid #fff; border-radius: 2px; position: relative; }
  .battery-icon::after { content: ""; position: absolute; left: 1px; top: 1px; bottom: 1px; width: 5px; background: #fff; }
  .app-header {
    background: var(--header-blue); color: var(--text-light);
    height: 82px; position: relative; text-align: center;
  }
  .stop-code { font-size: 21px; font-weight: 400; padding-top: 8px; }
  .stop-name { font-size: 21px; font-weight: 400; margin-top: 6px; }
  .stop-street { font-size: 11px; font-weight: 400; opacity: .9; margin-top: 1px; }
  .header-back { position: absolute; left: 14px; top: 44px; }
  .header-actions { position: absolute; right: 12px; top: 6px; display: flex; gap: 14px; align-items: center; }
  .location-strip { background: var(--header-blue); height: 34px; display: flex; }
  .location-tab { background: var(--subbar-blue); height: 34px; width: 58px; display: flex; align-items: center; justify-content: center; }
  .route-grid {
    display: grid; grid-template-columns: 1fr 1fr; gap: 8px;
    padding: 8px 8px 0;
  }
  .route-tile {
    height: 140px; position: relative; color: var(--text-light);
  }
  .route-tile .service-no {
    position: absolute; left: 0; right: 0; top: 18px; text-align: center;
    font-size: 40px; font-weight: 300; line-height: 1;
  }
  .route-tile .operator {
    position: absolute; left: 14px; bottom: 12px; font-size: 17px; font-weight: 400;
  }
  .arrivals {
    position: absolute; left: 0; right: 0; top: 74px;
    display: flex; justify-content: center; gap: 16px; list-style: none;
  }
  .arrival {
    display: flex; align-items: center; gap: 5px;
    font-size: 13px; font-weight: 500;
  }
  .seat-dot {
    width: 10px; height: 10px; border-radius: 50%;
    box-shadow: 0 0 0 1.5px var(--text-light);
  }
  .seat-available { background: var(--seat-available); }
  .seat-standing { background: var(--seat-standing); }
  .seat-full { background: var(--seat-full); }
  .wab-icon { width: 13px; height: 13px; fill: none; stroke: currentColor; }
  .tile-red { background: var(--tile-red); }
  .tile-purple { background: var(--tile-purple); }
  .tile-grey { background: var(--tile-grey); }
  .tile-grey.accent-red { color: var(--tile-red); }
  .tile-grey.accent-purple { color: var(--tile-purple); }
  .tile-empty { background: var(--tile-white); }
  .ad-banner {
    position: absolute; left: 0; right: 0; bottom: 0; height: 72px;
    background: linear-gradient(90deg, var(--ad-dark), var(--ad-light));
    color: var(--text-light);
    display: flex; align-items: center; justify-content: space-between; padding: 0 22px;
  }
  .ad-label { font-size: 18px; font-weight: 400; line-height: 1.15; }
  .ad-network { display: flex; align-items: center; gap: 8px; font-size: 17px; font-weight: 400; }
  .ad-network .mark { width: 22px; height: 22px; border-radius: 50%; background: var(--text-light); }
  .ad-network small { font-size: 9px; }
</style>
</head>
<body>
  <svg class="icon-defs" aria-hidden="true">
    <symbol id="icon-wheelchair" viewBox="0 0 24 24">
      <circle cx="11" cy="3.5" r="2.2" fill="currentColor" stroke="none"/>
      <path d="M11 7.5v6h5.5l2.5 6" stroke-width="2.4" stroke-linecap="round" stroke-linejoin="round"/>
      <path d="M8.5 10.5a6 6 0 1 0 7.5 7" stroke-width="2.4" stroke-linecap="round"/>
    </symbol>
  </svg>

  <main class="app-screen">
    <div class="status-bar">
      <span class="carrier"><span class="dots">●●●○○</span> KESTO
        <svg width="14" height="10" viewBox="0 0 14 10"><path d="M1 3.5a9 9 0 0 1 12 0M3.2 5.8a6 6 0 0 1 7.6 0M5.4 8a3 3 0 0 1 3.2 0" stroke="#fff" stroke-width="1.4" fill="none"/></svg>
      </span>
      <span class="clock">4:21 PM</span>
      <span class="battery">22% <span class="battery-icon"></span></span>
    </div>
    <header class="app-header">
      <svg class="header-back" width="14" height="22" viewBox="0 0 14 22"><path d="M12 2 3 11l9 9" stroke="#fff" stroke-width="2" fill="none"/></svg>
      <div class="header-actions">
        <svg width="26" height="26" viewBox="0 0 24 24"><path d="M12 2.5l2.9 6.3 6.8.7-5.1 4.6 1.5 6.8L12 17.4 5.9 20.9l1.5-6.8L2.3 9.5l6.8-.7z" fill="#fff"/></svg>
        <svg width="24" height="24" viewBox="0 0 24 24"><path d="M5 12a7 7 0 1 0 2.5-5.4" stroke="#fff" stroke-width="2.6" fill="none"/><path d="M4 3v6h6" stroke="#fff" stroke-width="2.6" fill="none"/></svg>
        <svg width="6" height="22" viewBox="0 0 6 22"><circle cx="3" cy="4" r="2.2" fill="#fff"/><circle cx="3" cy="11" r="2.2" fill="#fff"/><circle cx="3" cy="18" r="2.2" fill="#fff"/></svg>
      </div>
      <div class="stop-code">07589</div>
      <div class="stop-name">Opp rochor ctr</div>
      <div class="stop-street">oppir rd</div>
    </header>
    <div class="location-strip">
      <div class="location-tab">
        <svg width="16" height="20" viewBox="0 0 16 20"><path d="M8 19s6-6.5 6-11A6 6 0 0 0 2 8c0 4.5 6 11 6 11z" stroke="#fff" stroke-width="1.5" fill="none"/><circle cx="8" cy="8" r="2.2" stroke="#fff" stroke-width="1.5" fill="none"/></svg>
      </div>
    </div>

    <section class="route-grid">
      <div class="route-tile tile-red">
        <span class="service-no">48</span>
        <ul class="arrivals">
          <li class="arrival"><span class="seat-dot seat-available"></span>2 min<svg class="wab-icon"><use href="#icon-wheelchair"/></svg></li>
          <li class="arrival"><span class="seat-dot seat-standing"></span>11 min</li>
        </ul>
        <span class="operator">klv</span>
      </div>
      <div class="route-tile tile-red">
        <span class="service-no">57</span>
        <ul class="arrivals">
          <li class="arrival"><span class="seat-dot seat-full"></span>Arr<svg class="wab-icon"><use href="#icon-wheelchair"/></svg></li>
          <li class="arrival"><span class="seat-dot seat-available"></span>8 min<svg class="wab-icon"><use href="#icon-wheelchair"/></svg></li>
        </ul>
        <span class="operator">klv</span>
      </div>
      <div class="route-tile tile-red">
        <span class="service-no">131</span>
        <ul class="arrivals">
          <li class="arrival"><span class="seat-dot seat-standing"></span>5 min<svg class="wab-icon"><use href="#icon-wheelchair"/></svg></li>
          <li class="arrival"><span class="seat-dot seat-available"></span>16 min</li>
        </ul>
        <span class="operator">klv</span>
      </div>
      <div class="route-tile tile-grey accent-red">
        <span class="service-no">851</span>
        <ul class="arrivals">
          <li class="arrival"><span class="seat-dot seat-available"></span>3 min<svg class="wab-icon"><use href="#icon-wheelchair"/></svg></li>
          <li class="arrival"><span class="seat-dot seat-available"></span>12 min<svg class="wab-icon"><use href="#icon-wheelchair"/></svg></li>
        </ul>
        <span class="operator">dpwq</span>
      </div>
      <div class="route-tile tile-grey accent-purple">
        <span class="service-no">960</span>
        <ul class="arrivals">
          <li class="arrival"><span class="seat-dot seat-full"></span>4 min</li>
          <li class="arrival"><span class="seat-dot seat-standing"></span>9 min<svg class="wab-icon"><use href="#icon-wheelchair"/></svg></li>
        </ul>
        <span class="operator">dpwq</span>
      </div>
      <div class="route-tile tile-purple">
        <span class="service-no">2N</span>
        <ul class="arrivals">
          <li class="arrival"><span class="seat-dot seat-available"></span>7 min<svg class="wab-icon"><use href="#icon-wheelchair"/></svg></li>
          <li class="arrival"><span class="seat-dot seat-available"></span>22 min</li>
        </ul>
        <span class="operator">klv</span>
      </div>
      <div class="route-tile tile-purple">
        <span class="service-no">2N</span>
        <ul class="arrivals">
          <li class="arrival"><span class="seat-dot seat-standing"></span>14 min<svg class="wab-icon"><use href="#icon-wheelchair"/></svg></li>
          <li class="arrival"><span class="seat-dot seat-available"></span>30 min</li>
        </ul>
        <span class="operator">klv</span>
      </div>
      <div class="route-tile tile-empty"></div>
    </section>

    <aside class="ad-banner" role="img" aria-label="Test advertising banner with warm golden background">
      <span class="ad-label">320x50<br>Test Banner</span>
      <span class="ad-network"><span class="mark"></span>AdNest <small>by Veltrixa</small></span>
    </aside>
  </main>
</body>
</html>
```